Podcast Flyer and Business Cards

I need a like a 1/3 page vertical cardstock flyer advertising my podcast and business cards. I'd like 2 sets of each... each customized to show the books each co-host has written.

Basically a design for the card and a design for the flyer - all kind of similar

Target Market(s)

Therapy clients and students

Industry/Entity Type

Entertainment Industry

Font styles to use
Sans Serif

Colors
ec1f27

Requirements
Must have
• My logo
• see our website - www.velvetwavecouplescast.com
• My picture and cohost picture - must be retouched as my eyes are bloodshot.
• head size much match
• Use couple pic as top 1/4t of page on flyer.. and side by side podcast hosts on bottom. Will get you color of male cohost martin.
• on back of card 1 for Martin - must have his books
• on back of card 2 for Denise - must have her books
Nice to have
• red and black
• Martin - Author of Quiet Harbor, Gentle Burden, and co-author of Relationally Grounded Household Counseling

```html
<!DOCTYPE html>
<html lang="en">
<head>
<meta charset="utf-8">
<title>Velvet Wave – Podcast Flyers</title>
<link href="https://fonts.googleapis.com/css2?family=Bebas+Neue&family=PT+Sans:wght@400;700&display=swap" rel="stylesheet">
<style>
  :root{
    --red:#ec1f27;
    --black:#151515;
    --ink:#222;
    --paper:#f4f4f4;
    --gold:#f2b21c;
    --stage:#e6e4e1;
  }
  *{box-sizing:border-box;margin:0;padding:0}
  html,body{width:1200px;height:1132px;overflow:hidden}
  body{background:var(--stage);font-family:"PT Sans",sans-serif;color:var(--ink);position:relative}
  .flyer{position:absolute;top:100px;width:438px;height:917px;overflow:hidden;background:var(--paper);box-shadow:0 4px 14px rgba(0,0,0,.25)}
  .flyer--front{left:142px}
  .flyer--back{left:655px;background:linear-gradient(#cfcfcf 0,#f7f7f7 180px,#f7f7f7 100%)}
  .abs{position:absolute}
  .photo-couple{left:0;top:0;width:438px;height:440px;background:linear-gradient(160deg,#d8d8d8,#8a8a8a 55%,#5a5a5a)}
  .shape-layer{left:0;top:0}
  .logo{position:absolute;width:156px;height:156px;border-radius:50%;background:var(--black);border:4px solid #fff;display:flex;align-items:center;justify-content:center;text-align:center}
  .logo__name{font-family:"Bebas Neue",sans-serif;font-size:30px;line-height:1;color:#fff;letter-spacing:2px}
  .logo--front{left:21px;top:249px}
  .logo--back{left:325px;top:738px;width:102px;height:102px;border-width:3px}
  .logo--back .logo__name{font-size:20px}
  .title{position:absolute;left:0;width:100%;text-align:center;font-family:"Bebas Neue",sans-serif;white-space:nowrap;line-height:1}
  .title--front{top:436px;color:var(--ink);font-size:29px}
  .title--back{top:252px;color:var(--red);font-size:30px}
  .rule{position:absolute;height:1.5px;background:#333}
  .tagline{position:absolute;left:0;width:100%;text-align:center;font-size:21px;line-height:1.2}
  .tagline--front{top:472px;color:var(--ink)}
  .tagline--back{top:294px;color:var(--red)}
  .body-copy{position:absolute;text-align:justify;font-size:13px;line-height:1.22}
  .body-copy--front{left:24px;top:506px;width:390px}
  .body-copy--back{left:31px;top:355px;width:378px;font-size:13.6px;line-height:1.38}
  .body-copy--back p+p{margin-top:18px}
  .rank-band{left:0;top:604px;width:438px;height:98px;background:var(--red);color:#fff;text-align:center;font-weight:700;font-size:15px;line-height:1.3;padding-top:8px}
  .stars{color:var(--gold);font-size:20px;letter-spacing:1px;line-height:1}
  .pill{position:absolute;background:var(--black);color:#fff;border-radius:20px;text-align:center;font-weight:700;white-space:nowrap}
  .pill--subscribe{left:71px;top:685px;width:296px;height:37px;line-height:37px;font-size:18px;letter-spacing:.5px}
  .pill--tagline{left:68px;top:630px;width:302px;height:36px;line-height:36px;font-size:10.5px}
  .host{position:absolute;width:180px;text-align:center}
  .host__photo{width:104px;height:104px;border-radius:50%;border:3px solid #222;margin:0 auto 6px;background:linear-gradient(#c9a27a,#7d5f45)}
  .host__photo--denise{background:linear-gradient(#e9c08a,#b4784f)}
  .host__name{font-size:12.5px;color:#111}
  .host__role{font-size:8px;color:#444;margin-top:2px}
  .host--denise{left:21px;top:730px}
  .host--martin{left:225px;top:730px}
  .footer-band{left:0;top:883px;width:438px;height:34px;background:var(--black);color:#fff;text-align:center;font-size:14px;line-height:34px}
  .host--back{left:5px;top:30px}
  .host--back .host__photo{width:146px;height:146px;background:linear-gradient(#c9a27a,#6e5240)}
  .host--back .host__name{font-size:15px}
  .book{position:absolute;box-shadow:2px 3px 6px rgba(0,0,0,.35)}
  .book--burden{left:205px;top:50px;width:104px;height:160px;background:linear-gradient(#6fa3d9 0,#9ec3e6 40%,#d9a35b 70%,#c9853f)}
  .book--counseling{left:300px;top:58px;width:80px;height:150px;background:linear-gradient(#fafafa 0,#eef3ea 45%,#8fbf6a 70%,#3f8d3b)}
  .book--harbor{left:372px;top:64px;width:56px;height:142px;background:linear-gradient(#fff 0,#fff 40%,#2c8bd0 40%,#2c8bd0 56%,#f1f1f1 56%)}
  .rank-back{left:0;top:678px;width:100%;text-align:center;color:var(--red);font-weight:700;font-size:14.5px;line-height:1.3}
  .channels{left:0;top:854px;width:100%;text-align:center;color:var(--red);font-weight:700;font-size:16px;line-height:1.25}
</style>
</head>
<body>

<section class="flyer flyer--front">
  <div class="abs photo-couple" role="img" aria-label="Black and white photo of a couple embracing"></div>
  <svg class="abs shape-layer" width="438" height="917" viewBox="0 0 438 917">
    <path d="M0,330 Q230,320 438,392 L438,430 Q230,360 0,370 Z" fill="#ec1f27"/>
    <path d="M0,352 Q230,344 438,416 L438,917 L0,917 Z" fill="#f4f4f4"/>
  </svg>
  <div class="logo logo--front"><span class="logo__name">VELVET<br>WAVE</span></div>
  <h1 class="title title--front">Velvet Wave - Couples and Sex Therapy</h1>
  <div class="rule" style="left:38px;top:467px;width:362px"></div>
  <p class="tagline tagline--front">Helping couples keep it hot!</p>
  <p class="body-copy body-copy--front">An expert, frank and fascinating podcast about love and sex! Join us as we discuss relationship dynamics, therapy, heathy couples, marriage and family! Two international therapists bring you sound, concrete tools to find emotional connection and sexual eroticism. Fall in-love again. Rebuild trust. Feel desire.</p>
  <div class="abs rank-band">
    <div class="stars">★★★★★</div>
    TuneBox Rank : Top 10 in Sexuality Podcasts<br>&amp; Top 5 Couples Therapy Podcasts
  </div>
  <div class="pill pill--subscribe">SUBSCRIBE NOW!</div>
  <div class="host host--denise">
    <div class="host__photo host__photo--denise" role="img" aria-label="Portrait photo of Denise Harlow"></div>
    <div class="host__name">Denise Harlow, LMFT</div>
    <div class="host__role">Certified Sex Therapist</div>
  </div>
  <div class="host host--martin">
    <div class="host__photo" role="img" aria-label="Portrait photo of Martin Keane"></div>
    <div class="host__name">Martin Keane</div>
    <div class="host__role">EFT Trainer/Supervisor</div>
  </div>
  <div class="abs footer-band">www.velvetwavecouplescast.com</div>
</section>

<section class="flyer flyer--back">
  <div class="host host--back">
    <div class="host__photo" role="img" aria-label="Portrait photo of Martin Keane"></div>
    <div class="host__name">Martin Keane</div>
    <div class="host__role">EFT Trainer/Supervisor</div>
  </div>
  <div class="book book--harbor" role="img" aria-label="Book cover: Quiet Harbor"></div>
  <div class="book book--counseling" role="img" aria-label="Book cover: Relationally Grounded Household Counseling"></div>
  <div class="book book--burden" role="img" aria-label="Book cover: Gentle Burden"></div>
  <h2 class="title title--back">Velvet Wave - Couples and Sex Therapy</h2>
  <div class="rule" style="left:38px;top:285px;width:362px"></div>
  <p class="tagline tagline--back">Helping couples keep it hot!</p>
  <div class="body-copy body-copy--back">
    <p>A sex and relationship podcast to help committed couples keep it hot! Find hope and guidance to make your marriage or partnership both emotionally connected and sexually erotic. Join our Certified Sex Therapist Denise Harlow and couples therapist, EFT Supervisor and Trainer, Martin Keane for an expert, frank and fascinating conversation about love, sex, and relationship dynamics.</p>
    <p>We discuss everything from best sexual techniques to solving sexual and relational problems, Velvet Wave will help you fall in-love again, rebuild trust, and feel desire.</p>
  </div>
  <div class="pill pill--tagline">CONVERSATIONS YOU'VE ALWAYS WANTED TO HAVE</div>
  <div class="abs rank-back">
    <div class="stars" style="margin-bottom:4px">★★★★★</div>
    TuneBox Rank : Top 10 in Sexuality Podcasts<br>&amp; Top 5 Couples Therapy Podcasts
  </div>
  <svg class="abs shape-layer" width="438" height="917" viewBox="0 0 438 917" style="top:0">
    <rect x="0" y="745" width="438" height="172" fill="#151515"/>
    <path d="M0,745 L438,745 L438,888 Q240,790 0,790 Z" fill="#ec1f27"/>
    <path d="M0,745 L438,745 L438,872 Q240,776 0,776 Z" fill="#f7f7f7"/>
  </svg>
  <div class="logo logo--back"><span class="logo__name">VELVET<br>WAVE</span></div>
  <div class="abs channels">Found on TuneBox, Threadcast,<br>Orchard Audio, Soundwell and Lyrebox</div>
</section>

</body>
</html>
```